上記のような特長を持つ、弊店主力商品 「珪藻土コースター」を、定期販売する予定です。
主なターゲットは、飲食店さまです。

この珪藻土コースターは、吸水性とその高級感から、導入当初は喜ばれますが、しばらく使い続けていると、コースター表面上の目詰まりから、吸水性が悪くなることがわかってきました。

まとめて数十枚ご購入いただくと、飲食店様にとっては、そんなに安い買い物ではないと思っています。(弊店の売り上げにはなるので、もちろんうれしいのですが)

従いまして、コースターの吸水力が落ちてきたときに、そのコースターを新品と少しずつ交換できるようなプランがあれば、と思い珪藻土コースターの「毎月お届けコース」(定期購入プラン)を立ち上げることにいたしました。

つまりは、珪藻土コースターを導入された飲食店様に対して、定期的に数枚程度ご購入いただき、吸水性が悪くなったものを廃棄していただくことで、吸水力が高い状態を維持していただるようなプランをご提案したいと思っています。

つきまして、お願いしたいことは、この商品のサイト上の購入ページをデザインしていただけないか、ということでございます。
状況の説明等のテキスト文は、ある程度作りました。(添付:cst_monthly_story.txt)従いまして、添付したテキストを主に使っていただき、イラストや写真等を付加していただき、申し込みたくなるような商品購入ページ(毎月お届けプランを申し込みたくなるようなページ)をデザインしていただけないか、というお願いになります。

製作にあたりましての条件は下記になります
【諸条件について】
・添付したテキスト文をお使いいただき、レイアウトをお願いします。
・その他、ご自身で追加されたテキストを加えていただいても一向にかまいません。
・弊店サイトにある、テキストや写真は、如何様にでもアレンジしたりして使っていただいて結構です。
・説明等のため、独自のイラストや、写真などを付加していただけるとありがたいですが、納品いただいたコンテンツは、弊店サイトや、場合によってはチラシ等で流用させていただくこともあるかもしれませんので、著作権(もしくは、弊店での使用権)はフルにいただける状況でのご提案をお願いします。
・当デザインいただくページは、その内容柄、流用の上、複数のページができる予定です。(1枚のコース、2枚のコース や、オリジナルコースターのページ、●●絵柄のページなどなど)また、当方にて、加工・加筆修正等もさせていただくことがあります。また、弊社にて各所に流用されることを予めご承知おきくださいませ。

【納品物について】
・イラストレーターで写真等をレイアウトいただいた場合は、貼り付けた元画像(元イラスト)のデータも併せて納品をお願いいたします。(psd形式でも、aiでも、jpegでも結構です)イラストデータの場合は、こちらで拡大縮小することも考えられますので、aiデータをお願いします。
・デザイン(&レイアウト)が依頼のメインですので、イラストレーターファイルのみでも結構ですが、HTMLファイルででも納品いただければ、うれしいです(必須ではありません)
※要は、イラストレーターファイル、html もしくはその両方の納品をお願いします。
・イラストレーターのファイルは、当方環境の関係上、cs4 以下での保存での納品をお願いします。

以上です。

ご説明不足もあるかもしれません。
ご質問等あれば、是非くださいませ。

【その他】
場合によっては、今後、継続的にお願いさせていただくかもしれません。
可能であれば、
・過去に作ったことのあるページデザイン(作品)のurl
(商品ページでなくとも、トップでもランディングページでもなんでも結構です)
・直接依頼させていただくときのご希望の単価
も一緒にいただけると嬉しいです。(もちろん、なくともかまいませんので)

商品価格(●●円で結構です)、添付のテキストの内容
A4
片面
何がいいのか、含めて、ご提案お願いします。
• 高解像度JPG (.jpg)
• イラストレーター形式 (.ai)
一度、締め切りを経過したのですが、
誠に申し訳ありません、恐縮ながら納得できるものがありませんでしたので、延長させていただきました。こちらの依頼内容も説明が長いばっかりで、的を得ておらず、広すぎて良くなかったと思います。申し訳ありませんでした。

改めまして依頼内容を改めさせていただき、本追記内容をご参照の上、再提案頂戴できれば嬉しいです。何卒、よろしくお願い致します。
http://www.konobu-do.com/SHOP/KDTM-QX-ZLA07-03.html
(ID:mk、pw:zqx)
上記サイトをご覧頂き、
2箇所の画像箇所
・コースター毎月お届けコース1
・コースター毎月お届けコース2
の上記2箇所に入る、********************
※下の二箇所(コースターの写真、スケジュールサイクルの図 は ご提案不要です)
画像は、サイズを変更したりしますので、イラストレーターファイル(CS4以下)か、高解像度画像の納品をお願いします。

よろしくお願いします。
本依頼内容を、Webサイトのページ作成へ、カテゴリ変更させていただきます。それに伴い、増額させていただきました。
また、上記追記で、イラスト(等で、窓枠を埋める)2点の追加 をお願いしている形になっております。

もちろん、イラスト2点追加でもかまいませんし、それにとらわれなくとも結構です。本来は、「毎月購入コース」をご購入いただくためのページですので、それを喚起できるようであればどのようにデザインいただいてもかまいません。
(商品の仕様上の趣旨は変更できませんが。)

よろしくお願いいたします。

甲乙つけ難かったのですが、
弊店の弱点をうまく突いて(フォローして)いただけましたので、
決めました。

ご提案、誠にありがとうございました。
一つしか選べなくて心苦しいですが、
又の機会に、今後とも、よろしくお願いできれば幸いです。
ありがとうございました。

```html
<!DOCTYPE html>
<html lang="ja">
<head>
<meta charset="utf-8">
<title>珪藻土コースター 毎月お届けコース | 木延堂</title>
<link href="https://fonts.googleapis.com/css2?family=Noto+Sans+JP:wght@400;700;900&family=Noto+Serif+JP:wght@700&display=swap" rel="stylesheet">
<style>
:root{
  --bg:#ffffff;
  --text:#333333;
  --muted:#777777;
  --nav:#c9d7b3;
  --nav-dark:#7f9561;
  --side-head:#e6e6e6;
  --line:#d4d4d4;
  --blue:#2d6fb6;
  --teal:#3fb7b0;
  --sky:#4aa3df;
  --pink:#e9748e;
  --red:#d2352b;
  --orange:#f08c1e;
  --gold:#b99a4a;
  --cream:#f5f1e6;
  --mint:#e7f1ef;
}
*{box-sizing:border-box;margin:0;padding:0}
html,body{width:1200px;height:3176px;overflow:hidden}
body{background:var(--bg);color:var(--text);font-family:"Noto Sans JP",sans-serif;font-size:15px;position:relative}
.abs{position:absolute}

/* header */
.site-header{left:0;top:0;width:1200px;height:160px;border-bottom:1px solid var(--line)}
.brand{left:16px;top:18px;display:flex;align-items:center;gap:12px}
.brand-name{font-family:"Noto Serif JP",serif;font-weight:700;font-size:54px;color:#4b4b4b;letter-spacing:6px}
.brand-mark{width:44px;height:44px;background:var(--nav-dark)}
.tagline{left:20px;top:96px;font-size:15px;color:var(--nav-dark);letter-spacing:4px}
.search{left:470px;top:24px;display:flex;gap:8px}
.search input{width:260px;height:36px;border:1px solid #aaa;font-size:13px;padding:0 10px;font-family:inherit;color:#999}
.search button{width:64px;height:36px;background:#555;color:#fff;border:0;font-family:inherit;font-size:13px}
.contact{left:840px;top:12px;width:348px;height:62px;background:var(--blue);color:#fff;border-radius:6px;display:flex;align-items:center;gap:12px;padding:0 14px}
.contact small{font-size:11px;line-height:1.3;display:block}
.contact strong{font-size:27px;letter-spacing:1px}
.global-nav{left:0;top:160px;width:1200px;height:40px;background:var(--nav);display:flex}
.global-nav a{flex:1;text-align:center;line-height:40px;font-size:15px;font-weight:700;color:#3d4b2a;text-decoration:none;border-right:1px solid #fff}

/* sidebar */
.sidebar{left:0;top:210px;width:262px}
.side-block{margin-bottom:20px}
.side-title{background:var(--side-head);font-size:14px;font-weight:700;padding:6px 10px;border-left:4px solid var(--nav-dark)}
.side-list{list-style:none;padding:6px 10px;font-size:14px;line-height:1.75}
.side-list li::before{content:"› ";color:var(--muted)}
.side-search{padding:8px 10px;display:flex;gap:4px}
.side-search span{flex:1;height:26px;border:1px solid #bbb}
.side-search b{width:44px;height:26px;background:#777}
.banner-phone{background:var(--blue);color:#fff;height:200px;padding:14px;border-radius:4px}
.banner-phone h3{font-size:22px}
.banner-phone p{font-size:14px;line-height:1.6;margin-top:8px}
.banner-phone svg{margin-top:10px}
.banner-point{background:#fde9ee;border:2px solid var(--pink);height:170px;padding:14px;text-align:center;color:var(--pink)}
.banner-point p{font-size:13px;color:var(--text)}
.banner-point strong{font-size:46px;display:block;line-height:1.2}
.banner-aff{background:var(--teal);color:#fff;height:140px;padding:14px;text-align:center}
.banner-aff strong{font-size:44px;display:block}
.calendar{width:100%;border-collapse:collapse;font-size:13px;text-align:center}
.calendar td,.calendar th{border:1px solid var(--line);height:26px}
.calendar .sun{color:var(--red)}
.calendar .off{background:#fbd9d9}
.legend{font-size:13px;padding:6px 4px;line-height:1.6}
.legend i{display:inline-block;width:12px;height:12px;background:#fbd9d9;margin-right:4px;vertical-align:middle}
.side-company{border:1px solid var(--line);padding:14px;font-weight:700;font-size:16px;display:flex;gap:8px;align-items:center}
.side-company span.sq{width:18px;height:18px;background:var(--blue)}
.partner-badge{width:140px;height:60px;background:#333;margin:10px auto 0}

/* main */
.main{left:272px;top:210px;width:920px}
.hero{position:relative;height:550px;background:linear-gradient(180deg,#f1f6f3,#dfe9e6);border:1px solid var(--line)}
.hero-title{position:absolute;left:260px;top:30px;text-align:center}
.hero-title p{font-family:"Noto Serif JP",serif;font-size:22px;color:var(--gold)}
.hero-title h1{font-family:"Noto Serif JP",serif;font-size:58px;color:#6b5b2e;margin-top:6px}
.hero-photo{position:absolute;left:40px;top:150px;width:560px;height:300px;border-radius:50%;background:radial-gradient(ellipse at center,#ffffff 0%,#dbe6ea 55%,#9fb6c7 100%)}
.hero-points{position:absolute;left:640px;top:190px;list-style:none;font-size:17px;line-height:2;font-weight:700;color:#555}
.hero-points li::before{content:"● ";color:var(--teal)}
.hero-lead{position:absolute;left:0;bottom:24px;width:100%;text-align:center;font-size:18px;line-height:1.7}
.plan{position:relative;height:380px;margin-top:8px;background:linear-gradient(180deg,#fdf7ec,#f7ead2)}
.plan-head{position:absolute;left:0;top:14px;width:100%;text-align:center;font-size:30px;font-weight:900;color:var(--orange)}
.plan-badge{position:absolute;z-index:2;left:30px;top:80px;width:112px;height:112px;border-radius:50%;background:var(--orange);border:4px solid #fff;color:#fff;font-size:26px;font-weight:900;display:flex;align-items:center;justify-content:center;white-space:nowrap}
.plan-ribbon{position:absolute;z-index:1;left:150px;top:100px;width:740px;height:70px;background:var(--orange);color:#fff;display:flex;align-items:center;justify-content:center;gap:40px;font-size:36px;font-weight:900}
.plan-people{position:absolute;left:200px;top:190px;width:520px;height:180px;background:linear-gradient(180deg,#f8d9b8,#e8b37c);border-radius:90px 90px 0 0}
.merits{display:flex;justify-content:space-around;padding:34px 40px;height:300px}
.merit{width:230px;height:230px;border-radius:50%;color:#fff;text-align:center;display:flex;flex-direction:column;align-items:center;justify-content:center;font-weight:700;font-size:24px;line-height:1.4}
.merit svg{margin-bottom:8px}
.merit.teal{background:var(--teal)}
.merit.sky{background:var(--sky)}
.merit.pink{background:var(--pink)}
.notes{border:1px solid var(--line);padding:18px 22px;font-size:13px;line-height:1.75;height:420px}
.notes h2{font-size:14px;color:var(--blue);margin-bottom:6px}
.notes .red{color:var(--red)}
.product{display:flex;gap:30px;margin-top:30px;height:330px}
.product-photo{width:400px;height:260px;background:radial-gradient(ellipse at center,#ffffff,#cfdbe2);border-radius:4px}
.product-info{flex:1;font-size:14px}
.product-info h2{font-size:17px;color:var(--blue);line-height:1.5;border-bottom:1px solid var(--line);padding-bottom:8px}
.row{display:flex;border-bottom:1px solid var(--line);padding:8px 0}
.row dt{width:110px;color:var(--muted)}
.price{color:var(--red);font-weight:700;font-size:18px}
.qty{width:60px;height:26px;border:1px solid #aaa;display:inline-block;text-align:center;line-height:24px}
.btn-cart{display:inline-block;margin-top:14px;background:var(--orange);color:#fff;font-weight:700;padding:10px 26px;border-radius:4px}
.links{margin-top:12px;line-height:1.9;color:var(--blue)}
.thumbs{display:flex;gap:8px;margin-top:10px}
.thumbs span{width:60px;height:44px;background:#dfe7ec}
.pagetop{text-align:right;font-size:13px;color:var(--muted);padding:4px 0}

/* shopping info */
.guide{left:0;top:2330px;width:1200px;height:846px;border-top:3px solid var(--nav-dark);padding:18px 20px}
.guide h2{font-size:17px;color:var(--nav-dark);margin-bottom:14px}
.guide-cols{display:flex;gap:30px}
.guide-col{flex:1;font-size:13px;line-height:1.8}
.guide-col h3{font-size:15px;border-bottom:2px solid var(--nav);padding-bottom:4px;margin-bottom:8px}
.pay{width:100%;border-collapse:collapse;margin:10px 0;font-size:13px;text-align:center}
.pay td{border:1px solid var(--line);height:44px}
.pay td.label{background:var(--mint);font-weight:700}
.pay .chip{display:inline-block;width:52px;height:24px;background:#ddd;vertical-align:middle}
</style>
</head>
<body>

<header class="site-header abs">
  <div class="brand abs"><span class="brand-name">木延堂</span><span class="brand-mark"></span></div>
  <p class="tagline abs">日 本 の 暮 ら し を 彩 る 雑 貨 の 一 品</p>
  <div class="search abs"><input value="サイト内検索" aria-label="サイト内検索"><button>検索</button></div>
  <div class="contact abs">
    <svg width="30" height="30" viewBox="0 0 24 24" fill="#fff"><path d="M6.6 10.8a15 15 0 0 0 6.6 6.6l2.2-2.2a1 1 0 0 1 1-.25 11.4 11.4 0 0 0 3.6.6 1 1 0 0 1 1 1V20a1 1 0 0 1-1 1A17 17 0 0 1 3 4a1 1 0 0 1 1-1h3.5a1 1 0 0 1 1 1c0 1.25.2 2.45.6 3.6a1 1 0 0 1-.25 1z"/></svg>
    <div><small>ご注文・お問い合わせはお気軽に</small><strong>03-5512-7730</strong></div>
  </div>
</header>
<nav class="global-nav abs">
  <a>木延堂トップ</a><a>マイページ</a><a>お客様の声</a><a>ご利用ガイド</a><a>よくあるご質問</a><a>問い合わせる</a>
</nav>

<aside class="sidebar abs">
  <div class="side-block"><div class="side-title">商品検索</div><div class="side-search"><span></span><b></b></div></div>
  <div class="side-block"><div class="side-title">商品種類別</div>
    <ul class="side-list"><li>珪藻土コースター<br>　単品（1枚）<br>　組合わせ（4枚）<br>　コースターセット<br>　オリジナルコースター</li></ul></div>
  <div class="side-block"><div class="side-title">商品種類別</div>
    <ul class="side-list"><li>珪藻土コースター</li><li>珪藻土アロマプレート</li><li>珪藻土バスマット</li><li>ゆかいな調味料入れ</li><li>お得なセット</li></ul></div>
  <div class="side-block"><div class="side-title">価格帯別</div>
    <ul class="side-list"><li>6,000円〜</li><li>〜6,000円</li><li>〜3,000円</li><li>〜1,000円</li></ul></div>
  <div class="side-block banner-phone">
    <h3>お電話・FAX</h3>
    <p>でもお申し込み<br>いただけます</p>
    <svg width="80" height="50" viewBox="0 0 80 50"><rect x="2" y="10" width="50" height="36" rx="4" fill="none" stroke="#fff" stroke-width="3"/><rect x="56" y="4" width="20" height="42" rx="3" fill="#fff"/></svg>
    <p>お気軽にどうぞ</p>
  </div>
  <div class="side-block banner-point"><p>ご新規の<br>会員登録でいますぐ</p><strong>100円分</strong><p>のポイントプレゼント</p></div>
  <div class="side-block banner-aff"><p>アフィリエイターさん募集。</p><strong>10%</strong><p>の報酬をお支払い</p></div>
  <div class="side-block"><div class="side-title">注目キーワード</div>
    <p class="side-list" style="color:var(--blue)">珪藻土コースター オリジナルコースター 珪藻土バスマット 珪藻土アロマプレート</p></div>
  <div class="side-block"><div class="side-title">カレンダー</div>
    <table class="calendar">
      <tr><th colspan="7">＜2016年5月＞</th></tr>
      <tr><th class="sun">日</th><th>月</th><th>火</th><th>水</th><th>木</th><th>金</th><th>土</th></tr>
      <tr><td class="sun off">1</td><td>2</td><td class="off">3</td><td class="off">4</td><td class="off">5</td><td>6</td><td class="off">7</td></tr>
      <tr><td class="sun off">8</td><td>9</td><td>10</td><td>11</td><td>12</td><td>13</td><td class="off">14</td></tr>
      <tr><td class="sun off">15</td><td>16</td><td>17</td><td>18</td><td>19</td><td>20</td><td class="off">21</td></tr>
      <tr><td class="sun off">22</td><td>23</td><td>24</td><td>25</td><td>26</td><td>27</td><td class="off">28</td></tr>
      <tr><td class="sun off">29</td><td>30</td><td>31</td><td></td><td></td><td></td><td></td></tr>
    </table>
    <p class="legend"><i></i>休業日<br>土日祝日の発送はお休みです。<br>発送業務をお休みさせて頂く日は、このカレンダーで確認ください。</p></div>
  <div class="side-block"><div class="side-title">運営ショップ</div>
    <div class="side-company"><span class="sq"></span>木延堂株式会社</div>
    <div class="partner-badge"></div></div>
</aside>

<main class="main abs">
  <section class="hero">
    <div class="hero-title"><p>天然素材の珪藻土からできた</p><h1>驚きコースター</h1></div>
    <div class="hero-photo" role="img" aria-label="麻の葉柄の珪藻土コースターとグラスの写真"></div>
    <ul class="hero-points"><li>ぱっとすぐ吸水</li><li>見映えがする高級感</li><li>くり返し使える</li></ul>
    <p class="hero-lead">飲食店で……メンテナンス不要で新しいコースターを補充したい！<br>ご自宅で……毎月いろいろな柄のコースターを少しずつ集めたい！</p>
  </section>

  <section class="plan">
    <p class="plan-head">1枚からでもOK！安心の定期購入プラン</p>
    <div class="plan-badge">そこで</div>
    <div class="plan-ribbon"><span>毎月お届けコース</span><span>●●●●円</span></div>
    <div class="plan-people" role="img" aria-label="コースターを届ける配達員と受け取る店員のイラスト"></div>
  </section>

  <section class="merits">
    <div class="merit teal">
      <svg width="56" height="56" viewBox="0 0 56 56"><circle cx="28" cy="28" r="25" fill="none" stroke="#fff" stroke-width="4"/><text x="28" y="38" text-anchor="middle" font-size="28" fill="#fff" font-weight="700">¥</text></svg>
      通常購入より<br>●●円お得！</div>
    <div class="merit sky">
      <svg width="64" height="50" viewBox="0 0 64 50"><rect x="3" y="3" width="58" height="44" rx="3" fill="none" stroke="#fff" stroke-width="4"/><path d="M3 5l29 22L61 5" fill="none" stroke="#fff" stroke-width="4"/></svg>
      毎月15日に<br>メール便で配送</div>
    <div class="merit pink">
      <svg width="64" height="46" viewBox="0 0 64 46"><rect x="3" y="3" width="58" height="40" rx="5" fill="none" stroke="#fff" stroke-width="4"/><rect x="3" y="12" width="58" height="8" fill="#fff"/></svg>
      色々選べる♪<br>お支払方法</div>
  </section>

  <section class="notes">
    <h2>【コースの説明】</h2>
    <p class="red">この定期購入プランでは通常価格より割安で、毎月決まった枚数の珪藻土コースターをお届けします。吸水力が落ちたコースターを少しずつ新品と入れ替えることで、いつでも快適にお使いいただけます。</p>
    <p>■内容<br>商品名：珪藻土コースター（麻の葉柄）　●●枚セット<br>お届け日：毎月15日発送（土日祝日の場合は翌営業日）<br>お支払方法：クレジットカード・代金引換・銀行振込・コンビニ払い<br>配送方法：メール便（ポスト投函）にてお届けします。</p>
    <p>■ご注意<br>・お申し込みは、前月末日までの受付分から翌月の発送となります。<br>・コースの変更・解約は、お届け日の10日前までにご連絡ください。<br>・3回以上の継続をお願いしております。</p>
    <p>■お届け日について<br>初回のみ、お申し込み確認後順次発送いたします。2回目以降は毎月15日の発送となります。</p>
  </section>

  <section class="product">
    <div>
      <div class="product-photo" role="img" aria-label="麻の葉柄の珪藻土コースター4枚の商品写真"></div>
      <div class="thumbs"><span></span><span></span><span></span></div>
    </div>
    <div class="product-info">
      <h2>珪藻土コースター オリジナル 4枚【毎月お届けコース】驚きコースター</h2>
      <dl class="row"><dt>価格</dt><dd><span class="price">2,590円</span>（税込）</dd></dl>
      <dl class="row"><dt>ポイント</dt><dd style="color:var(--red)">［ポイント還元 26ポイント］</dd></dl>
      <dl class="row"><dt>購入数</dt><dd><span class="qty">1</span> セット</dd></dl>
      <span class="btn-cart">カートに入れる</span>
      <p class="links">› この商品について問い合わせる<br>› レビューを書きませんか？<br>› この商品について友達に知らせる</p>
    </div>
  </section>
  <p class="pagetop">page top</p>
</main>

<section class="guide abs">
  <h2>ショッピング インフォメーション</h2>
  <div class="guide-cols">
    <div class="guide-col">
      <h3>お支払い方法</h3>
      <p>以下のお支払い方法がご利用いただけます。</p>
      <table class="pay">
        <tr><td class="label">クレジットカード</td><td><span class="chip"></span> <span class="chip"></span> <span class="chip"></span> <span class="chip"></span></td></tr>
        <tr><td class="label">銀行振込</td><td class="label">郵便振替</td></tr>
        <tr><td class="label">代金引換</td><td class="label">コンビニ払い</td></tr>
      </table>
      <p>銀行振込・郵便振替は前払いとなります。入金確認後の発送となりますので、あらかじめご了承ください。代金引換の手数料はお客様のご負担となります。</p>
      <h3 style="margin-top:18px">送料・配送について</h3>
      <p>全国一律で配送いたします。一定金額以上のご購入で送料無料となります。メール便はポスト投函のため、日時指定はできません。</p>
    </div>
    <div class="guide-col">
      <h3>返品・交換について</h3>
      <p>・商品到着後、8日以内でお申し出いただいた場合のみ、返品を承ります。<br>・お客様都合による返品の場合、送料はお客様のご負担となります。<br>・不良品や誤配送の場合は、当店負担にて交換いたします。<br>・ご使用後の商品、お客様の責任で傷や汚れが生じた商品の返品はお受けできません。</p>
      <h3 style="margin-top:18px">個人情報の取り扱い</h3>
      <p>お預かりした個人情報は、商品の発送やご連絡のためにのみ使用し、第三者へ提供することはありません。</p>
      <h3 style="margin-top:18px">お問い合わせ</h3>
      <p>木延堂株式会社<br>TEL 03-5512-7730（平日 10:00〜17:00）</p>
    </div>
  </div>
</section>

</body>
</html>
```